A3 Event Poster for School Fundraiser

We are looking for a bold, engaging, and professional A3 poster design to promote a special school fundraising event. A top athlete will be visiting a primary school to inspire children, encourage participation in sport, and help launch a fundraising initiative to raise money for new PE/sports equipment for the school.

The poster will be displayed prominently outside the school and shared with parents and families. Its purpose is to generate excitement, explain the event quickly, and encourage parents/families to sponsor and get involved.

We work with about 50 different athletes so will need the design to be easy to alter the picture of the athlete/name etc so it can be replicated across the different athletes.

Target Market(s)

Priamary School Parents/Communities

Industry/Entity Type

Education

Font styles to use
Other font styles liked:
• The logo font is Rajdhani. ‘Corvel’ is bold, ‘Pennix’ is semibold and the strapline is regular.

Requirements
Must have
• Space for the Event Date (that school can write in themselves), A picture of the visiting athlete and their bio (with ability to easily change)
Nice to have
• Bold, eye-catching

```html
<!DOCTYPE html>
<html lang="en">
<head>
<meta charset="utf-8">
<title>Athlete Visit Fundraiser Poster</title>
<link rel="stylesheet" href="https://fonts.googleapis.com/css2?family=Rajdhani:wght@400;500;600;700&family=Arimo:ital,wght@1,700&display=swap">
<style>
  :root {
    --purple: #7b2d93;
    --purple-deep: #55206b;
    --purple-mid: #8c3fa6;
    --purple-text: #8a3aa0;
    --bio-text: #4a1a5c;
    --red: #e01e3c;
    --paper: #f3f5f8;
    --stripe: #dfe3e8;
    --stage: #e8e8ea;
    --white: #ffffff;
    --grey-text: #555a60;
  }
  * { margin: 0; padding: 0; box-sizing: border-box; }
  html, body {
    width: 1200px; height: 900px; overflow: hidden;
    background: var(--stage);
  }
  .poster {
    position: absolute; left: 320px; top: 18px;
    width: 560px; height: 864px;
    background: var(--paper);
    overflow: hidden;
    font-family: "Rajdhani", sans-serif;
    box-shadow: 0 2px 6px rgba(0,0,0,.15);
  }
  .backdrop { position: absolute; inset: 0; }
  .athlete-photo {
    position: absolute; left: 363px; top: 25px; width: 170px; height: 240px;
    background: linear-gradient(180deg, #6b4a3a 0%, #3a3f6a 45%, #2f5aa8 70%, #e9e9ee 100%);
  }
  .event-title {
    position: absolute; left: 29px; top: 266px;
    font-size: 32px; font-weight: 500; line-height: 42px;
    color: var(--purple-text);
  }
  .event-role {
    position: absolute; left: 29px; top: 406px;
    font-size: 36px; font-weight: 700; line-height: 40px;
    color: var(--red);
  }
  .athlete-name {
    position: absolute; right: 0; top: 265px; width: 275px; height: 64px;
    background: var(--red);
    clip-path: polygon(12% 0, 100% 0, 100% 100%, 0 100%);
    color: var(--white); font-size: 34px; font-weight: 700;
    display: flex; align-items: center; justify-content: flex-end;
    padding-right: 16px; letter-spacing: .5px;
  }
  .athlete-bio {
    position: absolute; right: 15px; top: 334px; width: 230px;
    text-align: right;
    font-family: "Arimo", sans-serif; font-style: italic; font-weight: 700;
    font-size: 17px; line-height: 24.6px; color: var(--bio-text);
  }
  .appeal-band {
    position: absolute; left: 0; top: 504px; width: 363px; height: 90px;
    background: var(--red);
    clip-path: polygon(0 0, 100% 0, 88% 100%, 0 100%);
    color: var(--white); font-size: 24px; font-weight: 600; line-height: 35px;
    padding: 10px 0 0 29px;
  }
  .values {
    position: absolute; left: 26px; top: 598px;
    display: flex; gap: 9px;
    font-size: 15px; font-weight: 500; color: var(--grey-text);
  }
  .values li { list-style: none; display: flex; align-items: center; gap: 3px; }
  .values li::before {
    content: ""; width: 10px; height: 10px; border-radius: 50%;
    background: var(--red); display: inline-block;
  }
  .mission-band {
    position: absolute; left: 0; top: 628px; width: 387px; height: 66px;
    background: var(--purple-deep);
    clip-path: polygon(0 0, 100% 0, 89% 100%, 0 100%);
    color: var(--white); font-size: 19px; font-weight: 600; line-height: 27px;
    padding: 6px 0 0 27px;
  }
  .date-band {
    position: absolute; left: 0; top: 694px; width: 322px; height: 42px;
    background: var(--purple);
    clip-path: polygon(0 0, 100% 0, 91% 100%, 0 100%);
    color: var(--white); font-size: 21px; font-weight: 700;
    display: flex; align-items: center; padding-left: 27px; letter-spacing: .3px;
  }
  .brand {
    position: absolute; left: 29px; top: 752px;
  }
  .brand-row { display: flex; align-items: center; gap: 8px; }
  .brand-dot {
    width: 34px; height: 34px; border-radius: 50%; background: var(--red);
  }
  .brand-name {
    font-size: 46px; font-weight: 700; line-height: 44px; color: var(--purple);
  }
  .brand-strap {
    margin-left: 42px; font-size: 16px; font-weight: 400; color: var(--purple);
  }
</style>
</head>
<body>
  <main class="poster">
    <svg class="backdrop" viewBox="0 0 560 864" width="560" height="864" aria-hidden="true">
      <g fill="var(--stripe)">
        <polygon points="70,260 400,0 470,0 70,315"/>
        <polygon points="230,230 520,0 560,0 560,20 290,230"/>
        <polygon points="360,480 560,325 560,380 395,510"/>
        <polygon points="330,690 560,510 560,560 370,700"/>
        <polygon points="370,730 560,580 560,620 410,740"/>
        <polygon points="145,864 420,650 470,650 195,864"/>
      </g>
      <polygon fill="var(--purple-deep)" points="0,0 320,0 0,275"/>
      <polygon fill="var(--purple)" points="0,0 190,0 0,160"/>
      <polygon fill="var(--purple-mid)" points="0,215 220,40 220,105 0,280"/>
      <polygon fill="var(--purple-mid)" points="195,125 345,0 385,0 195,160"/>
      <polygon fill="var(--purple)" points="140,150 240,80 240,130 140,205"/>
      <polygon fill="var(--purple)" points="290,85 395,0 420,0 290,110"/>
      <polygon fill="var(--purple)" points="340,140 560,-20 560,5 340,170"/>
      <polygon fill="var(--purple)" points="340,235 560,60 560,85 340,265"/>
      <polygon fill="var(--purple-deep)" points="560,555 560,864 290,864"/>
      <polygon fill="var(--purple)" points="560,650 560,864 390,864"/>
      <polygon fill="var(--purple-mid)" points="465,685 560,610 560,640 465,715"/>
      <polygon fill="var(--purple)" points="180,864 250,810 250,864"/>
      <polygon fill="var(--purple-deep)" points="255,864 300,820 300,864"/>
    </svg>

    <div class="athlete-photo" role="img" aria-label="Portrait photo of the visiting athlete wearing a team tracksuit jacket"></div>

    <h1 class="event-title">Inspirational<br>Athlete Visiting<br>Our School</h1>
    <h2 class="event-role">Olympic<br>Volleyball Player</h2>

    <div class="athlete-name">MARCUS ODUYA</div>
    <p class="athlete-bio">is a dynamic English volleyball player and coach, known for his leadership on and off the court and his passion for inspiring the next generation through sport</p>

    <div class="appeal-band">Help us raise funds<br>for new sports equipment</div>

    <ul class="values">
      <li>Be inspired</li>
      <li>Make a difference</li>
      <li>Get Active</li>
    </ul>

    <div class="mission-band">Inspiring every child to lead an active<br>resilient and healthy life</div>
    <div class="date-band">SUNDAY, APRIL 00TH | 0 PM</div>

    <div class="brand">
      <div class="brand-row">
        <span class="brand-dot"></span>
        <span class="brand-name">CorvelPennix</span>
      </div>
      <div class="brand-strap">Inspiring every child</div>
    </div>
  </main>
</body>
</html>
```